Basic Commercial & Residential Real Estate Web Site

I need a basic website for a new real estate company that deals with both residential and commercial sales. It must be clean and professional. We sell homes, office buildings, farms, and ranches. It should feel crisp and clean.
I need a main page with my logo and links to commercial, residential, farm and land searches with contact data forms. Also incorporated would be a mls property search (IDX) form. I am in Northern California and the current site I posted is at www.qlvantor.com. I need the functionality of the links and the supporting pages. I do not have all the copy ready because I did not know what to expect.
Updates

Project Deadline Extended
Reason: I apologize, I am extremely busy and you all need more data to do a good job. All the designs are great so far and it is extremely difficult to choose at this point. I haven't given you enough data. I haver now uploaded some relevent photos (not very good) and edited the brief. I am looking for what I call the Landing or main page with some functionality built in to other pages which I also need. Example if you click on "Commercial" it should go to a page that discusses our commercial dept.......

I would like to thank all the designers for all their hard work and efforts, I wish I could reward you all.

Thanks again for your creative and professional designs.

Frank

Target Market(s)

Corporate Execs for the Commercial Buildings
Homeowners/Families for the Homes and Farms
Upper end people for the land to build estates

Industry/Entity Type

Real Estate

Font styles to use
Sans Serif

Requirements
Must have
• Our Logo should be prominent, pronounced
Need contact data or button
Functional Page that links to other data pages
Must Have a "search for properties" feature
Must say "Commercial and Residential Representation"
Pictures of Commercial Building and Nice Home (Tradtional not contemporary)
Nice to have
• Individual Buttons or links to "Commercial, Residential, Farm/Ranch, Land"
Contact Data displayed
button that says "Maple Crest"-next to button is Maple Crest Logo-see www.maplecrest.bz
Links to "Buyers and "Sellers"
Links to Facebook, twitter,.....etc
Should not have
• 20+ story commercial buildings or ultra modern. See uploaded files of typical buildings for commercial.

```html
<!DOCTYPE html>
<html lang="en">
<head>
<meta charset="utf-8">
<title>Qlvantor Properties</title>
<link href="https://fonts.googleapis.com/css2?family=Open+Sans:wght@400;600;700&display=swap" rel="stylesheet">
<style>
:root{
  --page:#1b1b1b;
  --band:#141414;
  --panel:#262626;
  --footer:#101010;
  --blue:#1e9fe0;
  --blue-light:#46bdf2;
  --blue-dark:#0d7fc2;
  --text:#e9e9e9;
  --muted:#9a9a9a;
  --white:#ffffff;
}
*{margin:0;padding:0;box-sizing:border-box}
html,body{width:748px;height:1200px;overflow:hidden}
body{background:var(--page);font-family:"Open Sans",Arial,sans-serif;color:var(--text);position:relative}
.wrap{position:absolute;left:105px;width:543px}

.brand{position:absolute;top:30px;left:0;width:748px;text-align:center;font-size:26px;font-weight:600;letter-spacing:3px;color:var(--white)}

.main-nav{top:95px;height:30px;background:linear-gradient(var(--blue-light),var(--blue-dark));display:flex;border-radius:2px}
.main-nav a{flex:1;display:flex;align-items:center;justify-content:center;color:var(--white);font-size:11px;font-weight:700;text-decoration:none;border-right:1px solid rgba(255,255,255,.25)}
.main-nav a:last-child{border-right:none}

.hero{top:137px;height:213px;background:linear-gradient(100deg,#2f63a6 0%,#6fa6d9 45%,#a8cf7c 70%,#4f8a2e 100%)}
.hero-caption{position:absolute;left:14px;bottom:30px;background:rgba(20,20,20,.85);padding:9px 14px}
.hero-caption h2{font-size:15px;font-weight:700;color:var(--white)}
.hero-caption p{font-size:10px;color:#ddd}
.dots{position:absolute;bottom:10px;left:50%;transform:translateX(-50%);display:flex;gap:5px}
.dots span{width:7px;height:7px;border-radius:50%;background:#fff;opacity:.6}
.dots span:first-child{opacity:1}

.section-title{font-size:12px;font-weight:600;color:var(--blue)}
.sell-title{top:380px;text-align:center}
.sell-grid{top:406px;display:grid;grid-template-columns:repeat(4,1fr);gap:8px}
.sell-thumb{height:67px}
.sell-label{font-size:9px;color:var(--white);margin-top:8px;display:flex;align-items:center;gap:4px}
.sell-label i{width:0;height:0;border-left:4px solid var(--blue);border-top:3px solid transparent;border-bottom:3px solid transparent}

.homes-band{position:absolute;left:0;top:510px;width:748px;height:250px;background:var(--band)}
.homes-head{top:524px;display:flex;justify-content:space-between;align-items:center}
.arrows{display:flex;gap:4px}
.arrows span{width:14px;height:14px;background:var(--white);display:flex;align-items:center;justify-content:center}
.homes-grid{top:553px;display:grid;grid-template-columns:repeat(4,1fr);gap:8px}
.home-photo{height:69px}
.home-name{font-size:10px;font-weight:700;color:var(--white);margin-top:8px;white-space:nowrap}
.home-dev{font-size:8px;color:#ccc}
.home-price{font-size:8px;color:var(--blue-light);font-weight:600;white-space:nowrap}
.home-loc{font-size:8px;color:var(--white);font-weight:600;margin-top:3px}
.home-btns{display:flex;gap:4px;margin-top:5px}
.home-btns span{flex:1;background:var(--blue);color:var(--white);font-size:8px;font-weight:600;text-align:center;padding:4px 0}

.news-head{top:781px;width:352px;display:flex;justify-content:space-between;align-items:center}
.gallery-head{top:781px;left:468px;width:180px}
.news-grid{top:802px;width:352px;display:grid;grid-template-columns:1fr 1fr;gap:10px}
.news-photo{height:98px}
.news-text{font-size:8px;line-height:1.45;color:#ddd;margin-top:12px}
.news-more{font-size:8px;font-weight:700;color:var(--white);margin-top:8px}
.gallery{top:802px;left:468px;width:180px;height:156px;background:linear-gradient(160deg,#8fb9df,#3c6d9c 60%,#233f5c)}
.gallery-caption{position:absolute;left:0;right:0;bottom:0;background:rgba(15,15,15,.8);font-size:8px;font-weight:600;color:var(--white);padding:6px 8px}
.gallery-next{position:absolute;right:6px;top:64px;width:18px;height:18px;border-radius:50%;background:rgba(255,255,255,.85);display:flex;align-items:center;justify-content:center}

.site-footer{position:absolute;left:0;top:996px;width:748px;height:174px;background:var(--footer)}
.foot-brand{position:absolute;left:105px;top:46px;font-size:14px;font-weight:600;letter-spacing:1px;color:var(--white)}
.foot-col{position:absolute;top:28px;font-size:8px;line-height:2;color:#ccc}
.foot-col strong{color:var(--white)}
.foot-col a{display:block;color:#ccc;text-decoration:none}
.social{display:flex;gap:4px;margin-top:8px}
.social span{width:14px;height:14px;border-radius:50%}
.copyright{position:absolute;left:0;top:1170px;width:748px;height:30px;text-align:center;font-size:8px;color:var(--muted);line-height:30px}
.version{position:absolute;right:14px;top:0;font-size:8px}
</style>
</head>
<body>

<div class="brand">QLVANTOR PROPERTIES</div>

<nav class="wrap main-nav">
  <a href="#">Home</a><a href="#">Commercial</a><a href="#">Residential</a><a href="#">Farm</a><a href="#">Vacant Land</a><a href="#">Contact</a>
</nav>

<section class="wrap hero" role="img" aria-label="Glass office building beside green trees under a blue sky">
  <div class="hero-caption">
    <h2>We deal with both</h2>
    <p>residential and commercial sales</p>
  </div>
  <div class="dots"><span></span><span></span><span></span></div>
</section>

<h3 class="wrap section-title sell-title">What We Sell</h3>
<div class="wrap sell-grid">
  <div><div class="sell-thumb" role="img" aria-label="Luxury home with lawn" style="background:linear-gradient(#7fa8d6,#d9d2c0 55%,#4e7a35)"></div><div class="sell-label"><i></i>Luxury Homes</div></div>
  <div><div class="sell-thumb" role="img" aria-label="Office building" style="background:linear-gradient(#5f88c2,#b7c7d8 60%,#6d7a80)"></div><div class="sell-label"><i></i>Office Buildings</div></div>
  <div><div class="sell-thumb" role="img" aria-label="Farm fields" style="background:linear-gradient(#9cc2e4,#8fb156 55%,#5f7f2c)"></div><div class="sell-label"><i></i>Farms</div></div>
  <div><div class="sell-thumb" role="img" aria-label="Ranch land" style="background:linear-gradient(#a9c9e6,#c2a36b 55%,#7a5d33)"></div><div class="sell-label"><i></i>Ranches</div></div>
</div>

<div class="homes-band"></div>
<div class="wrap homes-head">
  <h3 class="section-title">Luxury Homes</h3>
  <div class="arrows">
    <span><svg width="6" height="8"><path d="M5 0 L1 4 L5 8" fill="none" stroke="#222" stroke-width="1.6"/></svg></span>
    <span><svg width="6" height="8"><path d="M1 0 L5 4 L1 8" fill="none" stroke="#222" stroke-width="1.6"/></svg></span>
  </div>
</div>
<div class="wrap homes-grid">
  <article>
    <div class="home-photo" role="img" aria-label="Villa with pool at dusk" style="background:linear-gradient(#3c5f8a,#c98f52 55%,#2a9bc7)"></div>
    <div class="home-name">Alder Ridge Manor</div><div class="home-dev">by Halvern Builders</div>
    <div class="home-price">$248,298.00 - $1,298,000.00</div><div class="home-loc">Brookvale, Oakmere</div>
    <div class="home-btns"><span>Buy Now</span><span>View Details</span></div>
  </article>
  <article>
    <div class="home-photo" role="img" aria-label="Modern house with pool" style="background:linear-gradient(#8fb8dc,#d9d9d4 50%,#3aa4cf)"></div>
    <div class="home-name">Alder Ridge Manor</div><div class="home-dev">by Halvern Builders</div>
    <div class="home-price">$248,298.00 - $1,298,000.00</div><div class="home-loc">Brookvale, Oakmere</div>
    <div class="home-btns"><span>Buy Now</span><span>View Details</span></div>
  </article>
  <article>
    <div class="home-photo" role="img" aria-label="Lit villa at evening" style="background:linear-gradient(#2f4f7a,#b9834c 55%,#5a4a36)"></div>
    <div class="home-name">Alder Ridge Manor</div><div class="home-dev">by Halvern Builders</div>
    <div class="home-price">$248,298.00 - $1,298,000.00</div><div class="home-loc">Brookvale, Oakmere</div>
    <div class="home-btns"><span>Buy Now</span><span>View Details</span></div>
  </article>
  <article>
    <div class="home-photo" role="img" aria-label="House with pool and terrace" style="background:linear-gradient(#7fa4cf,#cfc6b4 50%,#2f8fbf)"></div>
    <div class="home-name">Alder Ridge Manor</div><div class="home-dev">by Halvern Builders</div>
    <div class="home-price">$248,298.00 - $1,298,000.00</div><div class="home-loc">Brookvale, Oakmere</div>
    <div class="home-btns"><span>Buy Now</span><span>View Details</span></div>
  </article>
</div>

<div class="wrap news-head">
  <h3 class="section-title">Latest News</h3>
  <div class="arrows">
    <span><svg width="6" height="8"><path d="M5 0 L1 4 L5 8" fill="none" stroke="#222" stroke-width="1.6"/></svg></span>
    <span><svg width="6" height="8"><path d="M1 0 L5 4 L1 8" fill="none" stroke="#222" stroke-width="1.6"/></svg></span>
  </div>
</div>
<h3 class="wrap section-title gallery-head">Photo Gallery</h3>
<div class="wrap news-grid">
  <article>
    <div class="news-photo" role="img" aria-label="Traditional two-storey house" style="background:linear-gradient(#8cb3da,#c9c1ae 55%,#5d7d3a)"></div>
    <p class="news-text">Lorem ipsum is simply dummy text of the printing and typesetting industry. Lorem ipsum has been the industry's standard</p>
    <p class="news-more">Read More</p>
  </article>
  <article>
    <div class="news-photo" role="img" aria-label="Glass office tower" style="background:linear-gradient(#4f7fb5,#a9c4dd 55%,#55708a)"></div>
    <p class="news-text">Lorem ipsum is simply dummy text of the printing and typesetting industry. Lorem ipsum has been the industry's standard</p>
    <p class="news-more">Read More</p>
  </article>
</div>
<div class="wrap gallery" role="img" aria-label="Glass office building facade">
  <div class="gallery-next"><svg width="6" height="8"><path d="M1 0 L5 4 L1 8" fill="none" stroke="#222" stroke-width="1.6"/></svg></div>
  <div class="gallery-caption">Lorem ipsum is simply dummy text</div>
</div>

<footer class="site-footer">
  <div class="foot-brand">QLVANTOR</div>
  <div class="foot-col" style="left:219px"><a href="#">Home</a><a href="#">Commercial</a><a href="#">Residential</a><a href="#">Farm</a><a href="#">Vacant Land</a><a href="#">Contact</a></div>
  <div class="foot-col" style="left:311px"><a href="#">Privacy Policy</a><a href="#">Terms &amp; Conditions</a><a href="#">Disclaimer</a><a href="#">Legal Notice</a></div>
  <div class="foot-col" style="left:403px;line-height:1.6">
    <strong>Dana K. Ellery</strong><br>dana@qlvantor.com<br>(530) 555-0142<br>(530) 555-0187<br><br>
    <strong>Frank &amp; Marisol</strong><br>frank@qlvantor.com<br>(530) 555-0163
  </div>
  <div class="foot-col" style="left:518px">
    <strong>Connect With Us</strong>
    <div class="social">
      <span style="background:#d9483b"></span><span style="background:#f08a24"></span><span style="background:#2bb0e8"></span><span style="background:#1e8fc6"></span><span style="background:#3b5998"></span>
    </div>
  </div>
</footer>
<div class="copyright">© 2014 Company Name. All Rights Reserved<span class="version">v1</span></div>

</body>
</html>
```